Flyer for Merchant Capital Cash Advance business

Need Flyer Design to be advertised on Social Media Platforms and also Print it to Publish it in Magazines.
Flyer Will be printed in different sizes for different publications.
Size 1) 6.25 inches * 11 inches.
Size 2) 8 inch * 11 inch
Size 3) 8 inch * 5.5 I inch
Size 4) 5 inch * 7 inch.
Google “Merchant Capital Cash advance flyer pics” to get an idea.

Flyer Design for Merchant Cash advance business.

Merchant Cash Advance is alternate to bank loans and does not require Personal Guarantee or Collateral.
Updates

Need extra days to review

Target Market(s)

Business owners seeking loan.

Industry/Entity Type

Business Service

Font styles to use
Serif
Sans Serif
Decorative
Script

Colors

Designer to choose colors to be used in the design.

Requirements
Must have
• Content from the Files Uploaded.
• Sharp Colors.
Nice to have
• Would like to see flyer in shape of a Bank Check or a $100 Bill.
• Would like to show a Comparison between Bank Loan and MCA.
• Open to any other ideas.

```html
<!DOCTYPE html>
<html lang="en">
<head>
<meta charset="utf-8">
<title>Business Funding Made Easy – Flyer</title>
<link href="https://fonts.googleapis.com/css2?family=Rye&family=Open+Sans:wght@600;700&family=Lato:wght@400;700&display=swap" rel="stylesheet">
<style>
  :root {
    --page-bg: #b3c9b4;
    --paper-light: #e4e5c6;
    --paper-mid: #d6dab1;
    --paper-dark: #c9cfa0;
    --frame: #4c5a48;
    --ink: #2d2d2b;
    --title-fill: #d9d9cf;
    --green: #4a8a4a;
    --header-green: #4f8a4f;
    --row-gray: #cfcfcb;
    --row-green: #b8c398;
    --cell-line: #e9ead8;
    --tick: #3f8f46;
    --cross: #e0262b;
    --photo-a: #d9b9a2;
    --photo-b: #3f3a38;
  }
  * { box-sizing: border-box; margin: 0; padding: 0; }
  html, body { width: 1200px; height: 960px; overflow: hidden; background: var(--page-bg); }
  .canvas { position: relative; width: 1200px; height: 960px; }

  .flyer {
    position: absolute; left: 72px; top: 230px; width: 1058px; height: 499px;
    background: radial-gradient(ellipse at 45% 40%, var(--paper-light) 0%, var(--paper-mid) 60%, var(--paper-dark) 100%);
    overflow: hidden;
  }
  .frame { position: absolute; inset: 0; }

  .title {
    position: absolute; left: 58px; top: 60px;
    font-family: "Rye", serif; font-size: 43px; letter-spacing: 0.3px;
    color: var(--title-fill); -webkit-text-stroke: 2px var(--ink);
    text-shadow: 2px 2px 0 #6f705f; white-space: nowrap;
  }
  .subtitle {
    position: absolute; left: 59px; top: 110px;
    font-family: "Open Sans", sans-serif; font-weight: 700; font-size: 28px;
    color: var(--green); white-space: nowrap;
  }
  .subtitle-dark {
    position: absolute; left: 59px; top: 139px;
    font-family: "Open Sans", sans-serif; font-weight: 700; font-size: 27px;
    color: var(--ink); white-space: pre;
  }

  .comparison {
    position: absolute; left: 58px; top: 194px; width: 566px;
    border-collapse: collapse; font-family: "Lato", sans-serif;
    box-shadow: 2px 2px 3px rgba(0,0,0,0.25);
  }
  .comparison th {
    background: var(--header-green); color: #fff; font-weight: 400;
    font-size: 17px; height: 30px; text-align: left;
  }
  .comparison th.col-feature { padding-left: 28px; width: 247px; border-right: 2px solid var(--cell-line); }
  .comparison th.col-compare { padding: 0 0 0 46px; }
  .comparison th .vs { display: inline-block; margin: 0 16px 0 34px; }
  .comparison td { height: 22.5px; font-size: 11px; color: var(--ink); border-bottom: 1px solid var(--cell-line); }
  .comparison tr:nth-child(odd) td { background: var(--row-gray); }
  .comparison tr:nth-child(even) td { background: var(--row-green); }
  .comparison td.feature { padding-left: 29px; border-right: 2px solid var(--cell-line); line-height: 1.05; }
  .comparison td.mark { text-align: center; width: 162px; }
  .comparison td.mark + td.mark { border-left: 2px solid var(--cell-line); width: 157px; }
  .comparison tr.tall td { height: 29px; }
  .icon { width: 16px; height: 16px; vertical-align: middle; }

  .contact-line {
    position: absolute; left: 58px; top: 423px;
    font-family: "Lato", sans-serif; font-size: 14px; color: var(--ink); white-space: nowrap;
  }
  .contact-line .dots { letter-spacing: 0; color: #555; }

  .photo {
    position: absolute; left: 704px; top: 150px; width: 320px; height: 349px;
    background: linear-gradient(160deg, var(--photo-a) 0%, #c69d86 45%, var(--photo-b) 100%);
    border-radius: 150px 150px 0 0;
    opacity: 0.9;
  }
</style>
</head>
<body>
<div class="canvas">
  <section class="flyer">
    <svg class="frame" width="1058" height="499" viewBox="0 0 1058 499" aria-hidden="true">
      <rect x="28" y="30" width="1002" height="444" fill="none" stroke="var(--frame)" stroke-width="3"/>
      <rect x="35" y="37" width="988" height="430" fill="none" stroke="var(--frame)" stroke-width="1"/>
    </svg>

    <h1 class="title">BUSINESS FUNDING MADE EASY</h1>
    <p class="subtitle">A convenient alternative to Bank Loan</p>
    <p class="subtitle-dark">Business  Capital Cash Advance</p>

    <table class="comparison">
      <thead>
        <tr>
          <th class="col-feature">Business Capital</th>
          <th class="col-compare" colspan="2">Bank Loan<span class="vs">VS</span>Cash Advance</th>
        </tr>
      </thead>
      <tbody>
        <tr><td class="feature">No Personal Guarantee</td><td class="mark"><svg class="icon" viewBox="0 0 16 16"><circle cx="8" cy="8" r="8" fill="var(--tick)"/><path d="M4.3 8.3l2.4 2.4 5-5" fill="none" stroke="#fff" stroke-width="1.8"/></svg></td><td class="mark"><svg class="icon" viewBox="0 0 16 16"><circle cx="8" cy="8" r="8" fill="var(--cross)"/><path d="M5.2 5.2l5.6 5.6M10.8 5.2l-5.6 5.6" stroke="#fff" stroke-width="1.8"/></svg></td></tr>
        <tr><td class="feature">No Collateral  or Guarantors</td><td class="mark"><svg class="icon" viewBox="0 0 16 16"><circle cx="8" cy="8" r="8" fill="var(--tick)"/><path d="M4.3 8.3l2.4 2.4 5-5" fill="none" stroke="#fff" stroke-width="1.8"/></svg></td><td class="mark"><svg class="icon" viewBox="0 0 16 16"><circle cx="8" cy="8" r="8" fill="var(--cross)"/><path d="M5.2 5.2l5.6 5.6M10.8 5.2l-5.6 5.6" stroke="#fff" stroke-width="1.8"/></svg></td></tr>
        <tr><td class="feature">No Minimum Credit Score Required</td><td class="mark"><svg class="icon" viewBox="0 0 16 16"><circle cx="8" cy="8" r="8" fill="var(--tick)"/><path d="M4.3 8.3l2.4 2.4 5-5" fill="none" stroke="#fff" stroke-width="1.8"/></svg></td><td class="mark"><svg class="icon" viewBox="0 0 16 16"><circle cx="8" cy="8" r="8" fill="var(--cross)"/><path d="M5.2 5.2l5.6 5.6M10.8 5.2l-5.6 5.6" stroke="#fff" stroke-width="1.8"/></svg></td></tr>
        <tr><td class="feature">Simple One Page Application</td><td class="mark"><svg class="icon" viewBox="0 0 16 16"><circle cx="8" cy="8" r="8" fill="var(--tick)"/><path d="M4.3 8.3l2.4 2.4 5-5" fill="none" stroke="#fff" stroke-width="1.8"/></svg></td><td class="mark"><svg class="icon" viewBox="0 0 16 16"><circle cx="8" cy="8" r="8" fill="var(--cross)"/><path d="M5.2 5.2l5.6 5.6M10.8 5.2l-5.6 5.6" stroke="#fff" stroke-width="1.8"/></svg></td></tr>
        <tr><td class="feature">No Interest Rate (Flat Fee)</td><td class="mark"><svg class="icon" viewBox="0 0 16 16"><circle cx="8" cy="8" r="8" fill="var(--tick)"/><path d="M4.3 8.3l2.4 2.4 5-5" fill="none" stroke="#fff" stroke-width="1.8"/></svg></td><td class="mark"><svg class="icon" viewBox="0 0 16 16"><circle cx="8" cy="8" r="8" fill="var(--cross)"/><path d="M5.2 5.2l5.6 5.6M10.8 5.2l-5.6 5.6" stroke="#fff" stroke-width="1.8"/></svg></td></tr>
        <tr><td class="feature">Bankcruptcy OK</td><td class="mark"><svg class="icon" viewBox="0 0 16 16"><circle cx="8" cy="8" r="8" fill="var(--tick)"/><path d="M4.3 8.3l2.4 2.4 5-5" fill="none" stroke="#fff" stroke-width="1.8"/></svg></td><td class="mark"><svg class="icon" viewBox="0 0 16 16"><circle cx="8" cy="8" r="8" fill="var(--cross)"/><path d="M5.2 5.2l5.6 5.6M10.8 5.2l-5.6 5.6" stroke="#fff" stroke-width="1.8"/></svg></td></tr>
        <tr class="tall"><td class="feature">Opportunity to renew your cash advance<br>for additional funds</td><td class="mark"><svg class="icon" viewBox="0 0 16 16"><circle cx="8" cy="8" r="8" fill="var(--tick)"/><path d="M4.3 8.3l2.4 2.4 5-5" fill="none" stroke="#fff" stroke-width="1.8"/></svg></td><td class="mark"><svg class="icon" viewBox="0 0 16 16"><circle cx="8" cy="8" r="8" fill="var(--cross)"/><path d="M5.2 5.2l5.6 5.6M10.8 5.2l-5.6 5.6" stroke="#fff" stroke-width="1.8"/></svg></td></tr>
      </tbody>
    </table>

    <p class="contact-line">Business Name <span class="dots">...............................................</span> Email<span class="dots">........................................</span> Phone No<span class="dots">......................................</span></p>

    <div class="photo" role="img" aria-label="Photo of a smiling mother hugging her young daughter while holding a fan of hundred-dollar bills"></div>
  </section>
</div>
</body>
</html>
```